" A empresa tem foco prioritário na produção de alimentos (doces e salgados) para venda indireta, para distribuição, para fornecimento a ambientes com públicos que tem problemas relacionados a intolerâncias, alergias ou restrições alimentares, tais como restaurantes, lojas de produtos naturais, escolas, hospitais, eventos, etc, eventualmente contemplando a possibilidade futura de estabelecimento de ponto de atendimento fixo. "

```html
<!DOCTYPE html>
<html lang="pt-BR">
<head>
<meta charset="UTF-8">
<title>Forno Verdelha — Cartões</title>
<link href="https://fonts.googleapis.com/css2?family=Cormorant+Garamond:wght@500&family=Lato:wght@400&display=swap" rel="stylesheet">
<style>
  :root {
    --backdrop: #e9e9e9;
    --green: #1f6b3b;
    --red: #a8191f;
    --white: #fbfbfa;
    --ink-light: #f4f1ea;
    --ink-red: #a8191f;
    --ink-green: #1f6b3b;
  }
  * { margin: 0; padding: 0; box-sizing: border-box; }
  html, body { width: 1200px; height: 1200px; overflow: hidden; }
  body {
    background: var(--backdrop);
    position: relative;
    font-family: "Lato", sans-serif;
  }
  .card {
    position: absolute;
    width: 420px;
    height: 420px;
    border-radius: 50%;
    display: flex;
    flex-direction: column;
    align-items: center;
    justify-content: center;
    text-align: center;
    padding: 0 40px;
  }
  .card--green { left: 150px; top: 150px; background: var(--green); color: var(--ink-light); }
  .card--red   { left: 630px; top: 150px; background: var(--red); color: var(--ink-light); }
  .card--white { left: 390px; top: 630px; background: var(--white); color: var(--ink-red); border: 8px solid var(--green); }

  .brand-dot {
    width: 40px; height: 40px; border-radius: 50%;
    border: 3px solid currentColor;
    margin-bottom: 14px;
  }
  .brand-name {
    font-family: "Cormorant Garamond", serif;
    font-weight: 500;
    font-size: 50px;
    line-height: 1.05;
  }
  .tagline {
    font-family: "Cormorant Garamond", serif;
    font-weight: 500;
    font-size: 16px;
    letter-spacing: 2px;
    text-transform: uppercase;
    margin-top: 8px;
  }
  .card--white .tagline, .card--white .contact { color: var(--ink-green); }
  .contact {
    margin-top: 24px;
    font-size: 13px;
    line-height: 1.7;
    display: flex; flex-direction: column; align-items: center;
  }
  .contact-row { display: flex; align-items: center; gap: 8px; }
  .contact-dot { width: 8px; height: 8px; border-radius: 50%; background: currentColor; }
  .contact svg { width: 14px; height: 10px; }
</style>
</head>
<body>
  <article class="card card--green">
    <div class="brand-dot"></div>
    <div class="brand-name">Forno Verdelha</div>
    <div class="tagline">Doceria sem restrições</div>
    <div class="contact">
      <div class="contact-row"><span class="contact-dot"></span>@fornoverdelha</div>
      <div>Encomendas</div>
      <div class="contact-row">
        <svg viewBox="0 0 14 10"><rect x="0.5" y="0.5" width="13" height="9" fill="none" stroke="currentColor"/><path d="M0.5 0.5 L7 5.5 L13.5 0.5" fill="none" stroke="currentColor"/></svg>
        ola@fornoverdelha.com
      </div>
    </div>
  </article>

  <article class="card card--red">
    <div class="brand-dot"></div>
    <div class="brand-name">Forno Verdelha</div>
    <div class="tagline">Doceria sem restrições</div>
    <div class="contact">
      <div class="contact-row"><span class="contact-dot"></span>@fornoverdelha</div>
      <div>Encomendas</div>
      <div class="contact-row">
        <svg viewBox="0 0 14 10"><rect x="0.5" y="0.5" width="13" height="9" fill="none" stroke="currentColor"/><path d="M0.5 0.5 L7 5.5 L13.5 0.5" fill="none" stroke="currentColor"/></svg>
        ola@fornoverdelha.com
      </div>
    </div>
  </article>

  <article class="card card--white">
    <div class="brand-dot"></div>
    <div class="brand-name">Forno Verdelha</div>
    <div class="tagline">Doceria sem restrições</div>
    <div class="contact">
      <div class="contact-row"><span class="contact-dot"></span>@fornoverdelha</div>
      <div>Encomendas</div>
      <div class="contact-row">
        <svg viewBox="0 0 14 10"><rect x="0.5" y="0.5" width="13" height="9" fill="none" stroke="currentColor"/><path d="M0.5 0.5 L7 5.5 L13.5 0.5" fill="none" stroke="currentColor"/></svg>
        ola@fornoverdelha.com
      </div>
    </div>
  </article>
</body>
</html>
```